Business Card Design

We need a new business card design for a company based in Southlake, TX. We provide business consulting services in the information technology / services space. We like variations of the color blue, aqua, black, light tan, and white. Would like "cool" tones. The design should clearly communicate professionalism. Think outside the box - we don't want something "typical". Our company name is "Vantrell Advisory, LLC".
Updates

Thank you all for your submissions. We have seen some very creative and inspired designs. We have made a decision and will be moving forward with that design. Appreciate all of the hard work.

Industry/Entity Type

Information Technology

Contact Information for Business Card

Denise Harlow Trumbey
482 West Maple Ridge Dr.
Southlake, TX 76185

```html
<!DOCTYPE html>
<html lang="en">
<head>
<meta charset="utf-8">
<title>Vantrell Advisory, LLC — Business Card</title>
<link rel="stylesheet" href="https://fonts.googleapis.com/css2?family=PT+Sans+Narrow:wght@700&family=Source+Sans+3:wght@400&display=swap">
<style>
  :root {
    --aqua: #1dbfd1;
    --steel: #347294;
    --mist: #a9c3dc;
    --navy-ink: #3a4566;
    --ink: #111111;
    --paper: #ffffff;
  }
  html, body {
    margin: 0;
    padding: 0;
    width: 1200px;
    height: 702px;
    overflow: hidden;
    background: var(--paper);
  }
  .business-card {
    display: block;
    width: 1200px;
    height: 702px;
  }
  .aqua-band { fill: var(--aqua); }
  .steel-wedge { fill: var(--steel); }
  .mist-panel { fill: var(--mist); }
  .paper-stripe { fill: var(--paper); }
  .company-name {
    font-family: "PT Sans Narrow", "Arial Narrow", sans-serif;
    font-weight: 700;
    font-size: 97px;
    fill: var(--navy-ink);
  }
  .contact-name {
    font-family: "Source Sans 3", "Myriad Pro", sans-serif;
    font-size: 40px;
    fill: var(--ink);
  }
  .contact-address {
    font-family: "Source Sans 3", "Myriad Pro", sans-serif;
    font-size: 33px;
    fill: var(--ink);
  }
</style>
</head>
<body>
<svg class="business-card" viewBox="0 0 1200 702" xmlns="http://www.w3.org/2000/svg">
  <rect class="aqua-band" x="0" y="0" width="220" height="702"/>
  <polygon class="mist-panel" points="220,503 1200,560 1200,702 220,702"/>
  <polygon class="paper-stripe" points="0,479 1152,546 1200,560 220,503 0,488"/>
  <polygon class="steel-wedge" points="0,379 1152,546 0,479"/>

  <text class="company-name" x="247" y="135">Vantrell Advisory, LLC</text>
  <text class="contact-name" x="249" y="590">Denise Harlow Trumbey,</text>
  <text class="contact-address" x="249" y="645">482 West Maple Ridge Dr. Southlake, TX 76185</text>
</svg>
</body>
</html>
```